Unique Home Cooking School needs Wordpress Design

We need a wordpress design for our small business based in Singapore called Twirly Pebbles. It is a unique cooking school where the cooking course menu is completely customised to our client's preference/lifestyle/requests. More information can be found on our site: twirlypebbles.com

We are looking for something simple and easy to navigate. We are currently using a free template which we have customised ourselves. As the business is growing, we are looking to have a site more suited to our needs. The site should also be photo friendly, as we often post up photos of our food. It should also be social media integrated as a lot of our business is driven by QV.

The look and feel should really reflect the personalities of both owners - like the logo. Please feel free to contact us if you need more clarification.

Target Market(s)

Our target audience are usually female, with children, aged 25 - 45.
They are either stay-at-home mums or full-time mums that are keen to do more for the family.

Industry/Entity Type

Small Business

Requirements
Must have
• The wordpress design has to be able to accommodate food photos on every page.
It also needs to be able to support social media feeds within the site.
Should not have
• Design should not have any chef-like design elements as we are not chefs. We are two stay-home-mums wanting to impart skills to other stay-home-mums or domestic helpers.

```html
<!DOCTYPE html>
<html lang="en">
<head>
<meta charset="utf-8">
<title>Twirly Pebbles – About Us</title>
<link href="https://fonts.googleapis.com/css2?family=Arimo:ital,wght@0,400;0,700;1,400&family=Open+Sans:ital,wght@0,400;0,700;1,400&display=swap" rel="stylesheet">
<style>
:root{
  --navy:#0b3161;
  --navy-deep:#06244c;
  --ink:#222222;
  --body:#555555;
  --rule:#e4e4e4;
  --panel:#f0f0f0;
  --footer:#404349;
  --white:#ffffff;
}
*{margin:0;padding:0;box-sizing:border-box}
html,body{width:972px;height:1200px;overflow:hidden;background:var(--white)}
body{position:relative;font-family:"Arimo",Arial,sans-serif;color:var(--body)}
.abs{position:absolute}

/* navigation */
.nav{left:147px;top:0;height:42px;display:flex;gap:22px;align-items:center;font-size:9px;letter-spacing:.4px;color:var(--ink)}
.nav .current{position:relative}
.nav .current::after{content:"";position:absolute;left:50%;top:14px;margin-left:-3px;border:3px solid transparent;border-top:4px solid var(--navy)}
.social-top{left:776px;top:14px;display:flex;gap:8px}
.social-top span{width:12px;height:12px;border-radius:50%;background:var(--navy)}

/* header */
.brand-panel{left:0;top:42px;width:374px;height:167px;background:linear-gradient(135deg,#ececec,#dcdcdc)}
.brand-art{left:165px;top:54px;width:160px;height:96px;border-radius:8px;background:linear-gradient(135deg,#e7d5d0,#cfd6dc)}
.brand-name{left:0;width:466px;top:154px;text-align:center;font-family:"Open Sans",sans-serif;font-size:22px;color:#2b2b2b}
.brand-tag{left:0;width:466px;top:186px;text-align:center;font-size:8px;color:#333}
.hero{left:386px;top:42px;width:586px;height:167px;background:linear-gradient(100deg,#7aa22c 0%,#c8672a 30%,#b33d3e 50%,#6f9a33 75%,#3f7d22 100%)}
.hero-caption{left:386px;top:118px;width:233px;height:60px;background:rgba(0,0,0,.72);color:var(--white);padding:8px 10px}
.hero-caption h1{font-size:24px;font-weight:700;line-height:1.1}
.hero-caption p{font-size:10px;margin-top:4px}

/* main column */
.copy{left:159px;width:425px;font-size:8.4px;line-height:13.4px}
.copy p+p{margin-top:13.4px}
.clip{overflow:hidden}
.show-more{left:148px;width:439px;height:22px;background:#e6e6e6;text-align:center;font-size:10px;line-height:22px;color:#444}
.person{left:159px;font-size:14px;font-weight:700;color:var(--ink)}

/* recent blogs */
.blogs-title{left:598px;top:226px;font-size:24px;font-weight:700;color:#222}
.blog{left:600px;width:215px;height:60px}
.blog .thumb{position:absolute;left:0;top:0;width:39px;height:39px;border:1px solid #ddd;padding:2px;background:#fff}
.blog .thumb i{display:block;width:100%;height:100%}
.blog h3{position:absolute;left:50px;top:1px;font-size:8.5px;font-weight:700;color:var(--navy)}
.blog p{position:absolute;left:50px;top:15px;width:160px;font-size:7px;line-height:10.5px;color:#444}
.btn{background:var(--navy);color:var(--white);font-size:7px;text-align:center;box-shadow:0 1px 2px rgba(0,0,0,.3)}
.blog .btn{position:absolute;left:50px;top:41px;width:55px;height:16px;line-height:16px}

/* social feed + reviews */
.feed{left:148px;top:738px;width:226px;height:166px;background:var(--panel)}
.feed h2{position:absolute;left:17px;top:13px;font-family:"Open Sans",sans-serif;font-size:14px;font-weight:700;color:var(--navy)}
.feed .page-thumb{position:absolute;left:18px;top:36px;width:28px;height:28px;background:#fff;border:1px solid #ddd}
.feed .page-name{position:absolute;left:53px;top:35px;font-family:"Open Sans",sans-serif;font-size:9.5px;color:#3b5ba0}
.feed .like{position:absolute;left:53px;top:50px;width:26px;height:10px;background:#4a66a6;color:#fff;font-size:6.5px;line-height:10px;text-align:center}
.feed hr{position:absolute;left:18px;top:70px;width:190px;border:0;border-top:1px solid #999}
.feed .photos{position:absolute;left:18px;top:83px;width:183px;height:59px;background:linear-gradient(90deg,#8a6e5e,#2b4b8a,#8a6e5e,#2b4b8a,#c9c9c9)}
.reviews{left:386px;top:738px;width:439px;height:166px;background:var(--navy)}
.reviews h2{position:absolute;left:13px;top:13px;font-family:"Open Sans",sans-serif;font-size:14px;font-weight:700;color:var(--white)}
.quote{position:absolute;left:17px;top:40px;width:404px;height:96px;background:var(--navy-deep);padding:11px 14px;font-family:"Open Sans",sans-serif;font-style:italic;font-size:9.3px;line-height:17px;color:var(--white)}
.quote-tip{position:absolute;left:36px;top:136px}
.reviews .author{position:absolute;left:58px;top:142px;font-family:"Open Sans",sans-serif;font-style:italic;font-size:9px;color:var(--white)}

/* footer widgets */
.widget-title{font-family:"Open Sans",sans-serif;font-size:14px;font-weight:700;color:var(--ink);border-bottom:1px solid #aaa;padding-bottom:2px;top:953px}
.about-text{left:150px;top:998px;width:285px;font-size:8.2px;line-height:13.4px}
.about-btn{left:150px;top:1114px;width:54px;height:16px;line-height:16px}
.connect{left:459px;width:140px;height:30px;display:flex;align-items:center;gap:13px;font-size:9px;line-height:10px;color:#333}
.connect span.ring{width:29px;height:29px;border:1.5px solid #111;border-radius:50%;flex:none}
.updates-note{left:619px;top:994px;font-size:8px;color:#444}
.field{left:619px;width:207px;height:22px;border:1px solid #aaa;font-size:8px;line-height:20px;padding-left:11px;color:#555}
.subscribe{left:619px;top:1080px;width:74px;height:22px;line-height:22px;font-size:9.5px}

.bottom{left:0;top:1149px;width:972px;height:51px;background:var(--footer);color:var(--white);font-size:8.2px}
.bottom .copy-line{position:absolute;left:147px;top:20px}
.bottom .credit{position:absolute;right:147px;top:20px}
</style>
</head>
<body>

<nav class="abs nav">
  <span>HOME</span><span>ABOUT US</span><span class="current">COURESE</span><span>BLOG</span><span>CONTACT US</span>
</nav>
<div class="abs social-top" aria-label="Social links"><span></span><span></span><span></span></div>

<header>
  <div class="abs brand-panel"></div>
  <div class="abs brand-art" role="img" aria-label="Illustration of the two founders cooking"></div>
  <div class="abs brand-name" style="width:466px;left:0;text-align:center;width:466px;">Twirly Pebbles</div>
  <div class="abs brand-tag" style="width:466px">Cooking Lessons for Everyone</div>
  <div class="abs hero" role="img" aria-label="Photo of a wicker basket filled with fresh vegetables"></div>
  <div class="abs hero-caption">
    <h1>About Us</h1>
    <p>Cooking Lessons for Everyone</p>
  </div>
</header>

<main>
  <div class="abs copy clip" style="top:230px;height:105px">
    <p>We are two very Twirly Pebbles who share a passion for cooking and eating different foods, trying out new eateries and the love for collecting cookbooks! We believe that eating well and being able to provide our young families with delicious, healthy meals made at home is the foundation to general well-being.&nbsp; Since being Mums and whenever possible we try to make a lot from scratch to ensure only good things go into our children’s bodies. From mushy baby foods, to healthy sweet or savoury snacks to enticing meals that will interest them enough to eat it!</p>
    <p>On many of our experiences through food and in parenting, we met many people who shared this belief, yet lacked the confidence to do it at home. Once we felt we could have some time free of children, we were able to put together this</p>
  </div>
  <div class="abs show-more" style="top:342px">(show more)</div>

  <h2 class="abs person" style="top:372px">Rosalind</h2>
  <div class="abs copy" style="top:403px">
    <p>Rosalind is a greedy mum who believes in 5 official meal times in a day and secretly wishes she can regain her metabolic rate of her 18 year old self.&nbsp; She is also a full-time mum to two beautiful girls. Her older daughter believes in “happily ever afters” and loves avocado, pasta, pizza and sweet treats.&nbsp; Her younger daughter thinks that life is a stage and she is the lead actress and dancer.&nbsp; When she is not dancing and belting out songs from musicals, she can be found standing next to the refrigerator begging for cheese and crackers.</p>
  </div>
  <div class="abs show-more" style="top:475px">(show more)</div>

  <h2 class="abs person" style="top:510px">Marianne</h2>
  <div class="abs copy clip" style="top:541px;height:94px">
    <p>A food loving Mum who always looking for the positives in life. She’s a cook, assistant, driver, and social events organiser to a beautiful 4 year old who has a sophisticated palate that challenges her in the kitchen, and to a cute little 2 year old princess who should stay 2 forever.&nbsp; Wife, personal assistant and organiser to a wanna be professional golfer who in his spare time loves to watch footy on the TV and on his laptop (at the same time).</p>
    <p>Marianne loves to cook for her family and friends and as much as possible making it all from scratch. Recreating dishes with depth of flavour using only natural ingredients is a foodie achievement for her.&nbsp; She’s obsessed with reading food</p>
  </div>
  <div class="abs show-more" style="top:640px">(show more)</div>

  <aside>
    <h2 class="abs blogs-title">Recent Blogs</h2>
    <div class="abs blog" style="top:270px"><div class="thumb"><i role="img" aria-label="Photo of a baked dish" style="background:linear-gradient(135deg,#c9a04a,#7d6a2e)"></i></div><h3>Lorem Ipsum</h3><p>Lorem Ipsum is simply dummy text of the printing and typesetting industry.</p><div class="btn">Read More</div></div>
    <div class="abs blog" style="top:339px"><div class="thumb"><i role="img" aria-label="Photo of kitchen knives" style="background:linear-gradient(135deg,#9aa3ad,#3c4046)"></i></div><h3>Lorem Ipsum</h3><p>Lorem Ipsum is simply dummy text of the printing and typesetting industry.</p><div class="btn">Read More</div></div>
    <div class="abs blog" style="top:408px"><div class="thumb"><i role="img" aria-label="Photo of a cast iron pan" style="background:linear-gradient(135deg,#6b6b6b,#2a2a2a)"></i></div><h3>Lorem Ipsum</h3><p>Lorem Ipsum is simply dummy text of the printing and typesetting industry.</p><div class="btn">Read More</div></div>
    <div class="abs blog" style="top:478px"><div class="thumb"><i role="img" aria-label="Photo of a fresh salad" style="background:linear-gradient(135deg,#5f9a3a,#c0452e)"></i></div><h3>Lorem Ipsum</h3><p>Lorem Ipsum is simply dummy text of the printing and typesetting industry.</p><div class="btn">Read More</div></div>
    <div class="abs blog" style="top:547px"><div class="thumb"><i role="img" aria-label="Photo of a bowl of stew" style="background:linear-gradient(135deg,#c0662b,#7a3318)"></i></div><h3>Lorem Ipsum</h3><p>Lorem Ipsum is simply dummy text of the printing and typesetting industry.</p><div class="btn">Read More</div></div>
    <div class="abs blog" style="top:616px"><div class="thumb"><i role="img" aria-label="Photo of a rice dish" style="background:linear-gradient(135deg,#d9b45a,#8b4a22)"></i></div><h3>Lorem Ipsum</h3><p>Lorem Ipsum is simply dummy text of the printing and typesetting industry.</p><div class="btn">Read More</div></div>
  </aside>
</main>

<section class="abs feed">
  <h2>Like on QV</h2>
  <div class="page-thumb" role="img" aria-label="Page avatar"></div>
  <div class="page-name">Twirly Pebbles</div>
  <div class="like">Like</div>
  <hr>
  <div class="photos" role="img" aria-label="Grid of follower profile photos"></div>
</section>

<section class="abs reviews">
  <h2>Customer Reviews</h2>
  <blockquote class="quote">Lorem Ipsum has been the industry's standard dummy text ever since the 1500s, when an unknown printer took a galley of type and scrambled it to make a type specimen book. It has survived not only five centuries, but also the leap into electronic typesetting, remaining essentially unchanged. It was popularised in the 1960s with the release of Lettersheet sheets containing.</blockquote>
  <svg class="quote-tip" width="18" height="16" viewBox="0 0 18 16"><polygon points="0,0 18,0 0,16" fill="#06244c"/></svg>
  <div class="author">Author - 1</div>
</section>

<footer>
  <h2 class="abs widget-title" style="left:150px;width:287px">About Us</h2>
  <p class="abs about-text">We are two very Twirly Pebbles who share a passion for cooking and eating different foods, trying out new eateries and the love for collecting cookbooks! We believe that eating well and being able to provide our young families with delicious, healthy meals made at home is the foundation to general well-being.&nbsp; Since being Mums and whenever possible we try to make a lot from scratch to ensure only good things go into our children’s bodies. From mushy baby foods, to healthy sweet or savoury snacks to enticing meals that will interest them enough to eat it!</p>
  <div class="abs btn about-btn">Read More</div>

  <h2 class="abs widget-title" style="left:459px;width:134px">Connect With Us</h2>
  <div class="abs connect" style="top:995px"><span class="ring"></span><span>Find us On<br>QV</span></div>
  <div class="abs connect" style="top:1035px"><span class="ring"></span><span>Find us On<br>Chirper</span></div>
  <div class="abs connect" style="top:1075px"><span class="ring"></span><span>Find us On<br>Pinora</span></div>

  <h2 class="abs widget-title" style="left:617px;width:210px">Get Latest updates</h2>
  <p class="abs updates-note">Subscribe to Get our latest news</p>
  <div class="abs field" style="top:1019px">Name</div>
  <div class="abs field" style="top:1046px">Your Email Address</div>
  <div class="abs btn subscribe">Subscribe</div>

  <div class="abs bottom">
    <span class="copy-line">Copyright © 2014 Twirly Pebbles.</span>
    <span class="credit">Designed by Brightleaf Studio</span>
  </div>
</footer>

</body>
</html>
```